Breezy Trinkets Handcrafted Copper Jewelry

I make handcrafted copper bracelets and cuffs.
I need a banner made (2' 1/2" x 10')
I attached the logo (I would like that sketch to be purple)
Company name: Breezy Trinkets (in a "sassy" font)
Tag line: Wear your Breeze
Designer/Creator: Norma Tillery
481.307.6624
FB: www.friendpage.example/breezytrinkets
shop.breezytrinkets.example
I'd like the background to be white. I'm not sure what I'm looking for as far as the look or if I should add any pics of the copper jewelry that I make. I'm totally up for suggestions. I'm very eager to see how creative you can be.
Many thanks.
Jewelry

```html
<!DOCTYPE html>
<html lang="en">
<head>
<meta charset="utf-8">
<title>Breezy Trinkets Banner</title>
<link rel="stylesheet" href="https://fonts.googleapis.com/css2?family=Alex+Brush&family=Quicksand:wght@400;500&family=Nunito:wght@600;700&display=swap">
<style>
  :root {
    --bg: #ffffff;
    --plum: #7a3b91;
    --plum-mid: #9a5cb0;
    --lavender: #c9a6d6;
    --mist: #d9d9dd;
    --grey-text: #555555;
    --navy: #1e3a8a;
    --social: #3b5ba5;
    --copper-light: #c07a45;
    --copper-dark: #4a2a18;
  }
  html, body {
    margin: 0;
    padding: 0;
    overflow: hidden;
    background: var(--bg);
  }
  .banner {
    position: relative;
    width: 1200px;
    height: 300px;
    overflow: hidden;
    background: var(--bg);
  }
  .swoosh {
    position: absolute;
    inset: 0;
  }
  .figure-sketch {
    position: absolute;
    left: 40px;
    top: 8px;
    width: 115px;
    height: 284px;
    background: linear-gradient(180deg, rgba(154,92,176,0.18), rgba(154,92,176,0.32));
    border-radius: 50px 50px 10px 10px;
  }
  .mist-square {
    position: absolute;
    left: 35px;
    top: 148px;
    width: 88px;
    height: 118px;
    background: var(--mist);
    opacity: 0.55;
  }
  .brand-name {
    position: absolute;
    left: 135px;
    top: 6px;
    margin: 0;
    font-family: "Alex Brush", cursive;
    font-weight: 400;
    font-size: 102px;
    line-height: 1;
    color: var(--plum);
    white-space: nowrap;
  }
  .tagline {
    position: absolute;
    left: 485px;
    top: 118px;
    margin: 0;
    font-family: "Quicksand", sans-serif;
    font-size: 25px;
    color: var(--grey-text);
  }
  .role-label {
    position: absolute;
    left: 186px;
    top: 143px;
    margin: 0;
    font-family: "Quicksand", sans-serif;
    font-weight: 500;
    font-size: 19px;
    color: var(--grey-text);
  }
  .designer-name {
    position: absolute;
    left: 176px;
    top: 163px;
    margin: 0;
    font-family: "Alex Brush", cursive;
    font-size: 44px;
    color: var(--plum);
  }
  .phone {
    position: absolute;
    left: 176px;
    top: 248px;
    margin: 0;
    font-family: "Nunito", sans-serif;
    font-weight: 700;
    font-size: 26px;
    color: #ffffff;
  }
  .contact {
    position: absolute;
    left: 458px;
    top: 212px;
  }
  .social-mark {
    position: absolute;
    left: 0;
    top: 0;
    width: 34px;
    height: 34px;
    background: var(--social);
    border-radius: 3px;
  }
  .social-url {
    position: absolute;
    left: 45px;
    top: 14px;
    margin: 0;
    font-family: "Nunito", sans-serif;
    font-weight: 600;
    font-size: 20px;
    color: var(--navy);
    white-space: nowrap;
  }
  .shop-url {
    position: absolute;
    left: 45px;
    top: 40px;
    margin: 0;
    font-family: "Nunito", sans-serif;
    font-weight: 700;
    font-size: 24px;
    color: var(--navy);
    white-space: nowrap;
  }
  .product-grid {
    position: absolute;
    left: 945px;
    top: 5px;
    width: 243px;
    height: 290px;
    display: grid;
    grid-template-columns: 107px 107px;
    grid-template-rows: 88px 88px 88px;
    column-gap: 29px;
    row-gap: 12px;
  }
  .product-photo {
    background: radial-gradient(ellipse at 45% 45%, var(--copper-light), var(--copper-dark) 85%);
  }
</style>
</head>
<body>
<div class="banner">
  <svg class="swoosh" width="1200" height="300" viewBox="0 0 1200 300" aria-hidden="true">
    <path d="M0,165 C300,250 650,150 940,60 L940,100 C650,195 300,275 0,230 Z" fill="var(--lavender)" opacity="0.35"/>
    <path d="M0,228 C350,272 650,180 940,100 L940,150 C650,235 350,300 0,300 Z" fill="var(--plum-mid)"/>
    <path d="M140,300 C450,268 700,200 940,148 L940,166 C700,232 470,300 230,300 Z" fill="var(--lavender)" opacity="0.7"/>
    <path d="M0,300 L0,255 C200,268 330,262 420,250 C330,290 200,300 0,300 Z" fill="var(--plum)" opacity="0.6"/>
  </svg>

  <div class="mist-square"></div>
  <div class="figure-sketch" role="img" aria-label="Purple line sketch of a woman in a strapless dress and boots"></div>

  <h1 class="brand-name">Breezy Trinkets</h1>
  <p class="tagline">Wear your Breeze</p>

  <p class="role-label">Designer/Creator:</p>
  <p class="designer-name">Norma Tillery</p>

  <p class="phone">481.307.6624</p>

  <div class="contact">
    <div class="social-mark"></div>
    <p class="social-url">www.friendpage.example/breezytrinkets</p>
    <p class="shop-url">shop.breezytrinkets.example</p>
  </div>

  <div class="product-grid">
    <div class="product-photo" role="img" aria-label="Photo of an embossed copper cuff bracelet"></div>
    <div class="product-photo" role="img" aria-label="Photo of an embossed copper cuff bracelet"></div>
    <div class="product-photo" role="img" aria-label="Photo of an embossed copper cuff bracelet"></div>
    <div class="product-photo" role="img" aria-label="Photo of an embossed copper cuff bracelet"></div>
    <div class="product-photo" role="img" aria-label="Photo of an embossed copper cuff bracelet"></div>
    <div class="product-photo" role="img" aria-label="Photo of an embossed copper cuff bracelet"></div>
  </div>
</div>
</body>
</html>
```